Vexor Ridge website

i'm looking for a promotional website for my business.
we provide Rope Access, Work at Height & Difficult Access services.
we treat water leak into buildings, external renovation of buildings, windows cleaning, confined spaces services and practically jobs in which the access is difficult.
here are examples of web site i like :
http://www.pixelbarnwebs.example/site-themes/51827.html
http://www.pixelbarnwebs.example/page-templates/62914.html

Target Market(s)

private people, commercial household chiefs, maintenance managers

Industry/Entity Type

Business

Requirements
Must have
• - mobile friendly
- chatterbay redirection
- 5 tabs
- one more customizable page - so i can add a photo and a description of the service corresponding (for now i offer 7 different services)
- contact us on each page with no redirection
- we are offering 7 different services
the website will be published in Israel which means right to left or centered for english option in the future. (logo on left hand corner)

- no flash
- should be future customisable - for future
Nice to have
• - a space for a slogan
- non scrollable
- photos on the landing page + redirection to gallery (photos and short films)
- 3 dynamic banners with short description of the theme of each, clicking on the banner after it opened will redirect to it's corresponding page.

```html
<!DOCTYPE html>
<html lang="en">
<head>
<meta charset="utf-8">
<title>Vexor Ridge</title>
<link rel="stylesheet" href="https://fonts.googleapis.com/css2?family=PT+Sans+Narrow:wght@400;700&family=Open+Sans:wght@400;600&display=swap">
<style>
:root{
  --header-bg:#3b3b3b;
  --band:#000;
  --section-bg:#232323;
  --section-edge:#161616;
  --footer-bg:#3a3a3a;
  --text-light:#f2f2f2;
  --text-soft:#c9c9c9;
  --text-muted:#a9a9a9;
  --heading-gray:#bdbdbd;
  --rule:#8a8a8a;
  --link-blue:#3f8fd6;
  --btn-light:#dcdcdc;
  --hero-blue:#4a6fc4;
  --hero-stone:#cfc7bb;
}
*{box-sizing:border-box;margin:0;padding:0}
html,body{width:945px;height:1200px;overflow:hidden;background:#000}
body{font-family:"Open Sans",sans-serif;color:var(--text-light)}
.page{position:relative;width:945px;height:1200px;overflow:hidden}
.abs{position:absolute}
.narrow{font-family:"PT Sans Narrow",sans-serif}

/* header */
.site-header{left:0;top:0;width:945px;height:145px;background:linear-gradient(180deg,#414141,#363636)}
.brand{left:128px;top:48px;display:flex;align-items:center;gap:10px}
.brand-mark{width:34px;height:34px;border-radius:50%;background:#000}
.brand-name{font-family:"PT Sans Narrow",sans-serif;font-weight:700;font-size:30px;color:#000;line-height:1}
.lang{top:21px;display:flex;align-items:center;gap:5px;font-size:8px;color:var(--text-soft)}
.flag{width:24px;height:14px}
.search{left:590px;top:66px;display:flex;height:18px}
.search-input{width:185px;background:#fff;color:#999;font-size:8.5px;padding:3px 6px;line-height:12px}
.search-btn{width:50px;background:#000;color:#fff;font-size:9px;text-align:center;line-height:18px}
.main-nav{left:465px;top:100px;height:45px;display:flex;align-items:flex-end}
.nav-item{font-family:"PT Sans Narrow",sans-serif;font-size:13.5px;color:var(--text-light);padding:0 12px 5px;height:45px;display:flex;align-items:flex-end;border-right:1px solid #555}
.nav-item:last-child{border-right:none}
.nav-item.active{background:#000;border-radius:3px 3px 0 0;padding:0 18px 5px;border-right:none}
.band{left:0;width:945px;height:8px;background:var(--band)}

/* hero */
.hero{left:0;top:153px;width:945px;height:384px;background:linear-gradient(100deg,var(--hero-stone) 0%,#9fa6b3 30%,var(--hero-blue) 55%,#6f8fd8 75%,#e4ded4 100%)}
.hero-caption{left:0;top:322px;width:345px;height:135px;background:rgba(40,40,40,.72);padding:10px 22px 0}
.hero-title{font-family:"PT Sans Narrow",sans-serif;font-weight:700;font-size:22px;color:#fff;text-transform:uppercase;padding:0 0 2px 2px;border-bottom:1px solid #ddd;width:303px;line-height:27px}
.hero-text{font-size:9.6px;line-height:16.5px;color:#e0e0e0;margin-top:5px;width:305px}
.hero-arrow{top:457px;width:33px;height:32px;background:rgba(235,235,235,.85)}

/* services */
.services{left:0;top:545px;width:945px;height:510px;background:radial-gradient(ellipse at 50% 40%,#2d2d2d,var(--section-edge) 90%)}
.section-title{font-family:"PT Sans Narrow",sans-serif;font-size:21px;color:var(--heading-gray)}
.service-photo{width:133px;height:133px;border-radius:50%;border:3px solid #000;box-shadow:0 0 0 1px #444}
.service-label{font-family:"PT Sans Narrow",sans-serif;font-size:15px;line-height:16.5px;color:#d8d8d8}
.block-title{font-family:"PT Sans Narrow",sans-serif;font-size:17px;color:#d0d0d0;text-transform:uppercase;border-bottom:1px solid var(--rule);padding-bottom:2px}
.welcome-lead{font-size:10px;color:var(--text-soft)}
.welcome-text{font-size:7.9px;line-height:14.2px;color:var(--text-muted);text-align:justify;width:454px}
.btn-more{left:495px;top:990px;width:63px;height:25px;background:var(--btn-light);color:#111;font-family:"PT Sans Narrow",sans-serif;font-weight:700;font-size:12px;text-align:center;line-height:25px;border:1px solid #999}
.news-date{width:55px;height:55px;border-radius:50%;background:#000;color:#fff;font-size:10px;text-align:center;line-height:55px}
.news-text{font-size:8.2px;line-height:11px;color:var(--text-muted);text-align:justify;width:176px}
.news-more{font-size:8.5px;color:var(--link-blue)}

/* footer */
.site-footer{left:0;top:1055px;width:945px;height:145px;background:linear-gradient(180deg,#2e2e2e,var(--footer-bg) 25%)}
.footer-title{font-family:"PT Sans Narrow",sans-serif;font-weight:700;font-size:16px;color:#e8e8e8}
.news-input{left:108px;top:1113px;width:204px;height:25px;background:#fff;border-radius:3px;color:#888;font-style:italic;font-size:8px;padding:7px 12px}
.btn-subscribe{left:229px;top:1146px;width:82px;height:26px;background:#161616;color:#fff;font-family:"PT Sans Narrow",sans-serif;font-weight:700;font-size:12px;text-align:center;line-height:26px}
.social{left:600px;top:1089px;display:flex;gap:5px;justify-content:flex-end;width:241px}
.social-item{height:22px;min-width:22px;padding:0 3px;background:#4c4c4c;color:#e8e8e8;font-size:6.5px;line-height:22px;text-align:center;border-radius:2px}
.footer-links{right:104px;top:1124px;font-size:8.2px;color:#e0e0e0}
.copyright{right:104px;top:1146px;font-size:8.2px;color:#e0e0e0}
</style>
</head>
<body>
<div class="page">

  <header class="site-header abs">
    <div class="brand abs"><span class="brand-mark"></span><span class="brand-name">Vexor Ridge</span></div>

    <div class="lang abs" style="left:680px">
      <svg class="flag" viewBox="0 0 24 14" role="img" aria-label="Israel flag"><rect width="24" height="14" fill="#fff"/><rect y="2" width="24" height="2" fill="#2a57b8"/><rect y="10" width="24" height="2" fill="#2a57b8"/></svg>Israel
    </div>
    <div class="lang abs" style="left:760px">
      <svg class="flag" viewBox="0 0 24 14" role="img" aria-label="English flag"><rect width="24" height="14" fill="#1f3c8c"/><path d="M0 0L24 14M24 0L0 14" stroke="#fff" stroke-width="3"/><rect x="10" width="4" height="14" fill="#fff"/><rect y="5" width="24" height="4" fill="#fff"/><rect x="11" width="2" height="14" fill="#c8202f"/><rect y="6" width="24" height="2" fill="#c8202f"/></svg>English
    </div>

    <div class="search abs"><div class="search-input">type your word here</div><div class="search-btn">SEARCH</div></div>

    <nav class="main-nav abs">
      <span class="nav-item active">HOME</span>
      <span class="nav-item">ABOUT US</span>
      <span class="nav-item">SERVICES</span>
      <span class="nav-item">TESTIMONIALS</span>
      <span class="nav-item">CONTACT</span>
    </nav>
  </header>
  <div class="band abs" style="top:145px"></div>

  <section class="hero abs" role="img" aria-label="Rope access workers cleaning a curved glass facade, viewed from below"></section>
  <div class="hero-caption abs">
    <h1 class="hero-title">Lorem ipsum dolor sit amet, elit</h1>
    <p class="hero-text">Cum sociis natoque penatibus et magnis dis parturient montes, nascetur ridiculus mus. In iaculis facilisis massa. Etiam eu urna. Sed porta.Cum sociis natoque penatibus et magnis dis parturient montes, nascetur ridiculus mus. In iaculis facilisis massa. Etiam eu urna. Sed porta.</p>
  </div>
  <div class="hero-arrow abs" style="left:848px"><svg width="33" height="32" viewBox="0 0 33 32"><path d="M19 9l-7 7 7 7" fill="none" stroke="#777" stroke-width="1.5"/></svg></div>
  <div class="hero-arrow abs" style="left:888px"><svg width="33" height="32" viewBox="0 0 33 32"><path d="M14 9l7 7-7 7" fill="none" stroke="#777" stroke-width="1.5"/></svg></div>
  <div class="band abs" style="top:537px"></div>

  <section class="services abs"></section>
  <h2 class="section-title abs" style="left:100px;top:553px">Our Services</h2>

  <div class="service-photo abs" style="left:86px;top:606px;background:radial-gradient(circle,#d6dde6,#8ea6c4)" role="img" aria-label="Rope access technicians on a facade"></div>
  <div class="service-photo abs" style="left:246px;top:606px;background:radial-gradient(circle,#c9d2dc,#3f73b8)" role="img" aria-label="Workers at height beside a blue column"></div>
  <div class="service-photo abs" style="left:398px;top:606px;background:radial-gradient(circle,#4f6a6a,#1a2424)" role="img" aria-label="Interior of a building with leak repair equipment"></div>
  <div class="service-photo abs" style="left:559px;top:606px;background:linear-gradient(180deg,#8f96a0,#b89b7a 60%,#c4a57e)" role="img" aria-label="Rooftop view over a city during renovation"></div>
  <div class="service-photo abs" style="left:716px;top:606px;background:radial-gradient(circle,#dfe8f0,#3a87c8)" role="img" aria-label="Worker cleaning windows on a rope"></div>

  <div class="service-label abs" style="left:116px;top:754px">Rope Access</div>
  <div class="service-label abs" style="left:270px;top:746px">Work at Height &amp;<br>Difficult Access<br>services</div>
  <div class="service-label abs" style="left:429px;top:746px">Water Leak<br>into Buildings</div>
  <div class="service-label abs" style="left:582px;top:746px">External Renovation<br>of Buildings</div>
  <div class="service-label abs" style="left:745px;top:746px">Windows Cleaning</div>

  <h3 class="block-title abs" style="left:103px;top:839px;width:459px">Welcome to Vexor Ridge</h3>
  <p class="welcome-lead abs" style="left:103px;top:869px">Mauris vel lacus vitae felis vestibulum volutpat. Etiam est nunc, venisl.</p>
  <p class="welcome-text abs" style="left:103px;top:890px">Sed ut perspiciatis unde omnis iste natus error sit voluptatem accusantium doloremque laudantium, totam rem aperiam, eaque ipsa quae ab illo inventore veritatis et quasi architecto beatae vitae dicta sunt explicabo. Nemo enim ipsam voluptatem quia voluptas sit aspernatur aut odit aut fugit, sed quia consequuntur magni dolores eos qui ratione voluptatem sequi nesciunt. Neque porro quisquam est, qui dolorem ipsum quia dolor sit amet. Nemo enim ipsam voluptatem quia voluptas sit aspernatur aut odit aut fugit, sed quia consequuntur magni dolores eos qui ratione voluptatem sequi nesciunt. Neque porro quisquam est, qui dolorem ipsum quia dolor sit amet.</p>
  <div class="btn-more abs">learn more</div>

  <h3 class="block-title abs" style="left:605px;top:838px;width:232px">News</h3>
  <div class="news-date abs" style="left:603px;top:872px">Apr 17</div>
  <p class="news-text abs" style="left:663px;top:878px">Sed ut perspiciatis unde omnis iste natus error sit voluptatem accusantium doloremque rem aperiam, eaque ipsa quae ab illo inven.</p>
  <div class="news-date abs" style="left:603px;top:936px">Apr 17</div>
  <p class="news-text abs" style="left:663px;top:942px">Sed ut perspiciatis unde omnis iste natus error sit voluptatem accusantium doloremque rem aperiam, eaque ipsa quae ab illo inven.</p>
  <span class="news-more abs" style="left:795px;top:990px">More &gt;&gt;</span>

  <footer class="site-footer abs"></footer>
  <h4 class="footer-title abs" style="left:108px;top:1078px">Newsletter</h4>
  <div class="news-input abs">Your Email Id</div>
  <div class="btn-subscribe abs">Subscribe</div>

  <div class="social abs">
    <span class="social-item">chatterbay</span>
    <span class="social-item">Chirpline</span>
    <span class="social-item">Orbitly</span>
    <span class="social-item"><svg width="14" height="14" viewBox="0 0 14 14" style="vertical-align:middle"><circle cx="3" cy="11" r="1.6" fill="#f29a2e"/><path d="M2 6a6 6 0 0 1 6 6M2 2a10 10 0 0 1 10 10" fill="none" stroke="#f29a2e" stroke-width="1.8"/></svg></span>
    <span class="social-item">Pinmosaic</span>
    <span class="social-item"><svg width="14" height="14" viewBox="0 0 14 14" style="vertical-align:middle"><rect x="1" y="3" width="12" height="8" fill="none" stroke="#dfe6ee" stroke-width="1.2"/><path d="M1 3l6 5 6-5" fill="none" stroke="#dfe6ee" stroke-width="1.2"/></svg></span>
  </div>
  <div class="footer-links abs">Privacy &nbsp;| Terms of Use &nbsp;| &nbsp;FAQ &nbsp;| Contact Us</div>
  <div class="copyright abs">© 2013 Vexor Ridge, All rights reserved</div>

</div>
</body>
</html>
```